Oven Cleaning Business owner needs business card design

Hi there,
Would like for a business card to be designed for myself, the owner of a professional oven cleaning business on the Sunshine Coast.
Would like it to look sleek, and modern-ish. Bit creative is encouraged too.
Include following:
Name/title: Corin ter Haghe, Owner
Phone number: 1300 482 916
Email: info@hearthshinecrew.com.au
Website: www.hearthshinecrew.com.au

```html
<!DOCTYPE html>
<html lang="en">
<head>
<meta charset="utf-8">
<title>Hearthshine Crew — Business Card</title>
<link href="https://fonts.googleapis.com/css2?family=Archivo:wght@300;400;700;800&display=swap" rel="stylesheet">
<style>
  :root {
    --stage: #3a3b3d;
    --teal: #4bbcc4;
    --teal-deep: #2a7f86;
    --teal-mid: #3ea3aa;
    --ink: #111416;
    --paper: #ffffff;
    --paper-shade: #ececec;
    --rule: #8d9193;
  }
  * { box-sizing: border-box; margin: 0; padding: 0; }
  html, body { width: 1200px; height: 900px; overflow: hidden; }
  body {
    background: var(--stage);
    font-family: "Archivo", Arial, sans-serif;
    position: relative;
  }

  .card {
    position: absolute;
    width: 640px;
    height: 366px;
    left: 280px;
    border-radius: 30px 0 30px 0;
    overflow: hidden;
  }

  /* Back side */
  .card--back {
    top: 40px;
    background: radial-gradient(ellipse at 58% 42%, var(--teal) 0%, var(--teal-mid) 40%, var(--teal-deep) 100%);
  }
  .card--back .brand-mark {
    position: absolute;
    top: 120px;
    left: 0; right: 0;
    text-align: center;
    font-weight: 800;
    font-size: 26px;
    letter-spacing: 1px;
    text-transform: uppercase;
    color: var(--ink);
  }
  .card--back .site {
    position: absolute;
    right: 90px;
    top: 232px;
    color: var(--paper);
    font-weight: 400;
    font-size: 15px;
    letter-spacing: 5px;
  }
  .card--back .site-rule {
    position: absolute;
    left: 60px;
    right: 60px;
    top: 262px;
    height: 1px;
    background: rgba(255,255,255,0.85);
  }

  /* Front side */
  .card--front {
    top: 464px;
    background: linear-gradient(110deg, var(--paper-shade) 0%, var(--paper) 55%, var(--paper) 100%);
  }
  .person {
    position: absolute;
    left: 44px;
    top: 56px;
  }
  .person__name {
    font-weight: 700;
    font-size: 22px;
    letter-spacing: -0.5px;
    text-transform: uppercase;
    color: var(--ink);
  }
  .person__role {
    margin-top: 4px;
    font-weight: 300;
    font-size: 20px;
    color: var(--teal);
  }
  .contacts {
    position: absolute;
    left: 60px;
    top: 160px;
    list-style: none;
  }
  .contacts li {
    display: flex;
    align-items: center;
    gap: 10px;
    font-weight: 300;
    font-size: 18px;
    color: var(--ink);
    line-height: 30px;
  }
  .contacts svg { width: 16px; height: 16px; flex: none; }
  .contact-rule {
    position: absolute;
    left: 0;
    width: 380px;
    top: 262px;
    height: 1px;
    background: var(--rule);
  }
  .wordmark {
    position: absolute;
    left: 44px;
    top: 282px;
    display: flex;
    align-items: center;
    gap: 14px;
  }
  .wordmark__square {
    width: 22px;
    height: 22px;
    background: var(--teal);
  }
  .wordmark__name {
    font-weight: 800;
    font-size: 40px;
    letter-spacing: 1px;
    text-transform: uppercase;
    color: var(--ink);
  }
</style>
</head>
<body>

  <section class="card card--back" aria-label="Card back">
    <div class="brand-mark">Hearthshine Crew</div>
    <div class="site">www.hearthshinecrew.com.au</div>
    <div class="site-rule"></div>
  </section>

  <section class="card card--front" aria-label="Card front">
    <div class="person">
      <div class="person__name">Corin ter Haghe</div>
      <div class="person__role">Owner</div>
    </div>

    <ul class="contacts">
      <li>
        <svg viewBox="0 0 24 24" aria-hidden="true"><path fill="#4bbcc4" d="M6.6 10.8a15.2 15.2 0 0 0 6.6 6.6l2.2-2.2a1 1 0 0 1 1-.25 11.4 11.4 0 0 0 3.6.57 1 1 0 0 1 1 1V20a1 1 0 0 1-1 1A17 17 0 0 1 3 4a1 1 0 0 1 1-1h3.5a1 1 0 0 1 1 1c0 1.25.2 2.45.57 3.57a1 1 0 0 1-.25 1z"/></svg>
        1300 482 916
      </li>
      <li>
        <svg viewBox="0 0 24 24" aria-hidden="true"><rect x="2" y="5" width="20" height="14" rx="2" fill="#4bbcc4"/><path d="M3 6l9 7 9-7" fill="none" stroke="#fff" stroke-width="1.6"/></svg>
        info@hearthshinecrew.com.au
      </li>
      <li>
        <svg viewBox="0 0 24 24" aria-hidden="true"><circle cx="12" cy="12" r="10" fill="#4bbcc4"/><path d="M2 12h20M12 2c3 3 3 17 0 20M12 2c-3 3-3 17 0 20" fill="none" stroke="#fff" stroke-width="1.4"/></svg>
        www.hearthshinecrew.com.au
      </li>
    </ul>

    <div class="contact-rule"></div>

    <div class="wordmark">
      <span class="wordmark__square" aria-hidden="true"></span>
      <span class="wordmark__name">Hearthshine Crew</span>
    </div>
  </section>

</body>
</html>
```